Design some Business Cards for Zolva Parts

Need a professional two sided business card.
Must be designed in Adobe Illustrator.
Fonts and original design must be turned in if winning artwork has been chosen.

The company is distributes components such as : computer processors (CPU), RAM (Memory), Hard drives and motherboards; perhaps throw in some tech designs to be more impactful.

Details to be shown on card:

Name: Pera Lunvik
Title VP of Sales
T (555) XXX - XXXX
M (555) XXX - XXXX
E: sales@quorbel-supply.example

Office locations:
Canada, USA, Mexico, Netherlands, Shanghai, Hong Kong

************* FInal artwork must be submitted with the attached illustrator files. *************
************* One file per side must be submitted *************

```html
<!DOCTYPE html>
<html lang="en">
<head>
<meta charset="utf-8">
<title>Zolva Parts Business Cards</title>
<link rel="stylesheet" href="https://fonts.googleapis.com/css2?family=Roboto:wght@400;500;700&display=swap">
<style>
  :root {
    --page-bg: #d9d9d9;
    --card-bg: #f4f4f5;
    --brand-blue: #2b2f9e;
    --brand-navy: #1d2270;
    --text-dark: #3a3a3a;
    --text-grey: #555555;
    --band-grey: #6b6b6b;
    --band-grey-light: #9a9a9a;
    --decor-lilac: #dcdde9;
    --decor-lilac-dark: #b9bbd4;
  }
  * { margin: 0; padding: 0; box-sizing: border-box; }
  html, body {
    width: 1200px; height: 900px; overflow: hidden;
    background: var(--page-bg);
    font-family: "Roboto", Arial, sans-serif;
  }
  .canvas { position: relative; width: 1200px; height: 900px; }
  .card {
    position: absolute; left: 267px; width: 665px; height: 380px;
    background: var(--card-bg);
    box-shadow: 0 4px 14px rgba(0,0,0,0.18);
    overflow: hidden;
  }
  .card--locations { top: 45px; }
  .card--contact { top: 475px; }
  .card-art { position: absolute; inset: 0; width: 100%; height: 100%; }

  .brand-name {
    position: absolute;
    font-weight: 700; color: var(--brand-navy);
    letter-spacing: -0.5px; white-space: nowrap;
  }
  .card--locations .brand-name { left: 0; right: 0; top: 52px; text-align: center; font-size: 46px; }
  .card--contact .brand-name { left: 42px; top: 78px; font-size: 40px; }

  .locations-heading {
    position: absolute; left: 42px; top: 160px;
    font-size: 23px; color: var(--brand-blue); font-weight: 400;
  }
  .location-list { position: absolute; list-style: none; }
  .location-list li {
    display: flex; align-items: center; gap: 8px;
    font-size: 23px; color: var(--text-dark); height: 34px;
  }
  .location-list svg { width: 13px; height: 17px; flex: none; }
  .location-list--a { left: 48px; top: 195px; }
  .location-list--b { left: 215px; top: 180px; }
  .location-list--c { left: 440px; top: 140px; }

  .person { position: absolute; right: 40px; top: 38px; text-align: right; }
  .person-name { font-size: 22px; color: var(--brand-blue); font-weight: 400; }
  .person-title { font-size: 15px; color: var(--text-grey); margin-top: 4px; }

  .contact-list { position: absolute; left: 60px; top: 222px; list-style: none; }
  .contact-list li {
    display: flex; align-items: center; gap: 20px;
    font-size: 18px; color: var(--text-dark); height: 42px;
  }
  .contact-list svg { width: 24px; height: 22px; flex: none; }

  .decor-block {
    position: absolute; right: 60px; top: 100px; width: 170px; height: 170px;
    background: linear-gradient(to bottom, var(--decor-lilac) 0 70%, var(--decor-lilac-dark) 70% 100%);
  }
</style>
</head>
<body>
<main class="canvas">

  <section class="card card--locations" aria-label="Card side with office locations">
    <svg class="card-art" viewBox="0 0 665 380" aria-hidden="true">
      <defs>
        <linearGradient id="greyBand" x1="0" x2="1">
          <stop offset="0" stop-color="var(--band-grey-light)"/>
          <stop offset="1" stop-color="var(--band-grey)"/>
        </linearGradient>
      </defs>
      <path d="M330 380 L330 350 Q340 325 380 322 L665 310 L665 380 Z" fill="url(#greyBand)"/>
      <path d="M0 380 L0 355 L330 340 Q355 338 372 350 L372 380 Z" fill="var(--brand-blue)"/>
    </svg>

    <div class="brand-name">Zolva Parts</div>
    <h2 class="locations-heading">Office Locations :</h2>

    <ul class="location-list location-list--a">
      <li><svg viewBox="0 0 12 16"><path d="M6 0a6 6 0 0 0-6 6c0 4.5 6 10 6 10s6-5.5 6-10a6 6 0 0 0-6-6z" fill="var(--brand-blue)"/><circle cx="6" cy="6" r="2.2" fill="#fff"/></svg>Canada</li>
      <li><svg viewBox="0 0 12 16"><path d="M6 0a6 6 0 0 0-6 6c0 4.5 6 10 6 10s6-5.5 6-10a6 6 0 0 0-6-6z" fill="var(--brand-blue)"/><circle cx="6" cy="6" r="2.2" fill="#fff"/></svg>Mexico</li>
    </ul>
    <ul class="location-list location-list--b">
      <li><svg viewBox="0 0 12 16"><path d="M6 0a6 6 0 0 0-6 6c0 4.5 6 10 6 10s6-5.5 6-10a6 6 0 0 0-6-6z" fill="var(--brand-blue)"/><circle cx="6" cy="6" r="2.2" fill="#fff"/></svg>Netherlands</li>
      <li><svg viewBox="0 0 12 16"><path d="M6 0a6 6 0 0 0-6 6c0 4.5 6 10 6 10s6-5.5 6-10a6 6 0 0 0-6-6z" fill="var(--brand-blue)"/><circle cx="6" cy="6" r="2.2" fill="#fff"/></svg>USA</li>
    </ul>
    <ul class="location-list location-list--c">
      <li><svg viewBox="0 0 12 16"><path d="M6 0a6 6 0 0 0-6 6c0 4.5 6 10 6 10s6-5.5 6-10a6 6 0 0 0-6-6z" fill="var(--brand-blue)"/><circle cx="6" cy="6" r="2.2" fill="#fff"/></svg>Shanghai</li>
      <li><svg viewBox="0 0 12 16"><path d="M6 0a6 6 0 0 0-6 6c0 4.5 6 10 6 10s6-5.5 6-10a6 6 0 0 0-6-6z" fill="var(--brand-blue)"/><circle cx="6" cy="6" r="2.2" fill="#fff"/></svg>Hong Kong</li>
    </ul>
  </section>

  <section class="card card--contact" aria-label="Card side with contact details">
    <svg class="card-art" viewBox="0 0 665 380" aria-hidden="true">
      <path d="M175 0 L365 0 Q355 12 335 12 L195 12 Q180 12 175 0 Z" fill="var(--brand-blue)"/>
      <path d="M275 380 Q280 362 300 360 L440 356 Q462 356 470 380 Z" fill="var(--brand-blue)"/>
    </svg>

    <div class="person">
      <div class="person-name">PERA LUNVIK</div>
      <div class="person-title">VP of Sales</div>
    </div>

    <div class="brand-name">Zolva Parts</div>
    <div class="decor-block"></div>

    <ul class="contact-list">
      <li><svg viewBox="0 0 24 24"><path d="M6.6 2.5l3 3.2-1.8 2.6c1.2 2.8 3.2 4.9 6 6.2l2.5-1.8 3.2 3-2 3.4C10 18.4 5.2 13.5 4 4.6z" fill="var(--brand-navy)"/></svg>(555) XXX - XXXX</li>
      <li><svg viewBox="0 0 24 24"><path d="M6.6 2.5l3 3.2-1.8 2.6c1.2 2.8 3.2 4.9 6 6.2l2.5-1.8 3.2 3-2 3.4C10 18.4 5.2 13.5 4 4.6z" fill="var(--brand-navy)"/></svg>(555) XXX - XXXX</li>
      <li><svg viewBox="0 0 24 18"><rect x="1" y="1" width="22" height="16" fill="none" stroke="var(--brand-navy)" stroke-width="2"/><path d="M1 1l11 9 11-9" fill="none" stroke="var(--brand-navy)" stroke-width="2"/></svg>sales@quorbel-supply.example</li>
    </ul>
  </section>

</main>
</body>
</html>
```